Gold Harbor Concierge

I need a website developed for our travel concierge service. I'm looking to be able to collect information and have the information collected directed to a inbox. I would also like to me able to manage the updates to the website myself. I also would like a mobile version of the website to be included. Our services include assistance with Bachelor Parties, Bachelorette Parties and Medical Tourism. We provide custom packages that include Airport Transportation, Lodging, Bilingual guides and any other special needs identified by our clients.
Industry/Entity Type
Travel
Coding
Coded - Design and coding required
Number of Pages Required
4 page
Look and feel

```html
<!DOCTYPE html>
<html lang="en">
<head>
<meta charset="utf-8">
<title>Gold Harbor Concierge – Website Design</title>
<link rel="stylesheet" href="https://fonts.googleapis.com/css2?family=Playfair+Display:wght@400;700&family=Montserrat:wght@400;600;700&display=swap">
<style>
:root{
  --board:#1b1b1b;
  --dark:#222222;
  --dark-2:#2c2c2c;
  --panel:#363636;
  --light:#eef2f5;
  --white:#ffffff;
  --gold:#e0a02e;
  --ink:#1c1c1c;
  --muted:#9a9a9a;
}
*{margin:0;padding:0;box-sizing:border-box}
html,body{width:1200px;height:3054px;overflow:hidden;background:var(--board)}
body{position:relative;font-family:"Montserrat",sans-serif;color:var(--ink)}
.serif{font-family:"Playfair Display",serif}
.abs{position:absolute}
.frame{position:absolute;overflow:hidden}
.photo{position:absolute}
.btn{position:absolute;border:1px solid var(--white);color:var(--white);font:700 5px "Montserrat",sans-serif;letter-spacing:.08em;display:flex;align-items:center;justify-content:center;box-shadow:2px 2px 0 var(--white)}
.btn.dark{border-color:var(--ink);color:var(--ink);box-shadow:2px 2px 0 var(--ink);background:var(--white)}
.btn.gold{background:var(--gold);border:none;box-shadow:none}
.center{left:0;right:0;text-align:center}
.brand{font-family:"Playfair Display",serif;color:var(--white);white-space:nowrap}
.brand-dot{display:inline-block;width:7px;height:7px;border-radius:50%;background:var(--gold);margin-right:4px;vertical-align:middle}

/* ---------- Desktop ---------- */
.desktop{left:333px;top:640px;width:584px;height:1752px;background:var(--dark)}
.desktop .hero{left:0;top:0;width:584px;height:227px}
.hero-photo{left:0;top:0;width:584px;height:227px;background:linear-gradient(120deg,#3b4a52 0%,#6b5a45 35%,#c9b08a 55%,#4a3a30 80%,#2a2d30 100%)}
.hero-menu{right:64px;top:24px;text-align:right;font:400 5px "Playfair Display",serif;color:var(--ink);line-height:13px}
.hero-menu .label{font-size:6.5px;text-decoration:underline;margin-bottom:6px;line-height:10px}
.hero-contact{right:64px;top:168px;text-align:right;font:600 4.5px "Montserrat",sans-serif;color:var(--ink);line-height:8px}
.hero-contact .addr{font-weight:400;margin-top:5px;line-height:6px}
.hero-kicker{left:63px;top:91px;font:400 11px "Playfair Display",serif;color:var(--white)}
.hero-title{left:63px;top:104px;font:700 19px/22px "Playfair Display",serif;color:var(--white)}
.hero-sub{left:63px;top:152px;font:400 4.5px "Montserrat",sans-serif;color:var(--white)}

.welcome{left:0;top:227px;width:584px;height:265px;background:linear-gradient(180deg,#262626,#1e1e1e)}
.kicker{font:400 7px "Playfair Display",serif}
.title{font:700 18px "Playfair Display",serif}
.para{font:400 5px/9px "Montserrat",sans-serif}

.services-bg{left:0;top:352px;width:584px;height:380px}
.service-card{position:absolute;top:525px;width:140px;height:155px}
.service-photo{left:0;top:0;width:134px;height:83px}
.service-name{left:0;top:91px;font:400 8.5px "Playfair Display",serif}
.service-text{left:0;top:106px;width:130px;font:400 4.5px/7px "Montserrat",sans-serif}
.dots{position:absolute;font:700 8px sans-serif;letter-spacing:1px;line-height:4px}

.packages{left:0;top:730px;width:584px;height:300px;background:linear-gradient(180deg,#2a2a2a,#1f1f1f)}
.pkg{position:absolute;top:110px;width:146px;height:157px}
.pkg-photo{left:0;top:0;width:146px;height:157px}
.pkg-panel{left:30px;top:5px;width:86px;height:125px;background:var(--panel);text-align:center;color:var(--white)}
.pkg-icon{width:30px;height:30px;border-radius:50%;background:var(--gold);margin:26px auto 0;border:2px solid #f2d9a6}
.pkg-name{font:700 6.5px "Playfair Display",serif;margin-top:9px}
.pkg-text{font:400 4px/6px "Montserrat",sans-serif;margin:5px 8px 0;color:#ddd}
.pkg-plus{position:absolute;left:38px;bottom:-4px;width:10px;height:10px;background:var(--white);color:var(--ink);font:700 7px/10px sans-serif;text-align:center}

.news{left:0;top:1030px;width:584px;height:335px;background:var(--white)}
.news-item{position:absolute}
.news-tag{display:inline-block;background:var(--gold);color:var(--white);font:600 3.5px/5px "Montserrat",sans-serif;padding:0 5px;border-radius:3px;margin-bottom:4px}
.news-title{display:block;font:400 7px/9px "Playfair Display",serif;color:var(--white)}

.contact{left:0;top:1365px;width:584px;height:220px;background:var(--light)}
.form-card{left:219px;top:53px;width:302px;height:167px;background:var(--white);box-shadow:0 2px 8px rgba(0,0,0,.12)}
.field{position:absolute;border:1px solid #888;font:400 4.5px "Montserrat",sans-serif;padding:4px 5px;color:var(--ink)}
.submit{position:absolute;background:var(--ink);color:var(--white);font:700 5px "Montserrat",sans-serif;display:flex;align-items:center;justify-content:center;letter-spacing:.05em}

.footer{left:0;top:1585px;width:584px;height:167px;background:linear-gradient(180deg,#262626,#1c1c1c)}
.f-col{position:absolute;top:42px;color:var(--white)}
.f-col h4{font:400 7.5px "Playfair Display",serif;margin-bottom:8px}
.f-col p{font:400 4.5px/11px "Montserrat",sans-serif;color:#ddd}
.social{display:flex;gap:5px}
.social span{width:13px;height:13px;border-radius:50%;background:var(--white);display:block}

/* ---------- Mobile ---------- */
.mobile{left:102px;top:402px;width:163px;height:1833px;background:var(--dark)}
.m-bar{left:0;top:0;width:163px;height:40px;background:#151515}
.m-burger{right:8px;top:10px;width:18px;height:18px;border-radius:3px;background:#333;display:flex;flex-direction:column;justify-content:center;gap:2.5px;padding:0 4px}
.m-burger i{display:block;height:1.5px;background:var(--white)}
.m-arrow{position:absolute;font:400 10px sans-serif;color:var(--ink)}
.m-arrow.w{color:var(--white)}
.m-form-field{position:absolute;left:8px;width:133px;height:22px;border:1px solid #888;font:400 5px "Montserrat",sans-serif;padding:6px 6px;color:var(--ink)}
</style>
</head>
<body>

<!-- ================= MOBILE ================= -->
<section class="frame mobile" aria-label="Mobile layout">
  <div class="abs m-bar">
    <div class="abs brand" style="left:7px;top:13px;font-size:10px"><span class="brand-dot"></span>Gold Harbor</div>
    <div class="abs m-burger"><i></i><i></i><i></i></div>
  </div>

  <div class="photo" role="img" aria-label="Friends toasting champagne on a yacht deck" style="left:0;top:40px;width:163px;height:86px;background:linear-gradient(120deg,#3b4a52,#7a6850 45%,#c7ae88 60%,#3a3230)"></div>
  <svg class="abs" style="left:0;top:40px" width="163" height="86"><polygon points="120,0 128,0 158,58 154,66" fill="#fff"/><polygon points="150,0 163,0 163,86 160,86" fill="#fff"/></svg>
  <div class="abs serif" style="left:7px;top:50px;font-size:6px;color:#fff">Gold Harbor</div>
  <div class="abs serif" style="left:7px;top:61px;font:700 9.5px/13px 'Playfair Display',serif;color:#fff">Travel Concierge<br>Service</div>
  <div class="btn" style="left:7px;top:98px;width:48px;height:12px">READ MORE</div>

  <div class="abs" style="left:0;top:126px;width:163px;height:240px;background:linear-gradient(180deg,#2a2a2a,#1e1e1e)"></div>
  <div class="abs center kicker" style="top:136px;color:#fff;font-size:6.5px">Welcome To</div>
  <div class="abs center serif" style="top:148px;color:#fff;font:700 10.5px 'Playfair Display',serif">Gold Harbor Concierge</div>
  <div class="abs center" style="top:170px;padding:0 8px;color:#ddd;font:400 5px/9px 'Montserrat',sans-serif">Neque porro quisquam est, qui dolorem ipsum quia dolor sit amet, consectetur, adipisci velit, sed quia non numquam eius modi tempora incidunt ut labore et dolore magnam aliquam quaerat voluptatem. Nemo enim ipsam voluptatem quia voluptas sit aspernatur aut odit aut fugit, sed quia consequuntur.</div>
  <div class="btn" style="left:56px;top:258px;width:50px;height:14px">READ MORE</div>

  <svg class="abs" style="left:0;top:278px" width="163" height="290"><polygon points="0,85 163,0 163,290 0,290" fill="#eef2f5"/></svg>
  <div class="abs center kicker" style="top:342px;font-size:6.5px">We Arrange</div>
  <div class="abs center title" style="top:353px;font-size:11px">Special Services</div>
  <div class="abs center" style="top:377px;padding:0 8px;font:400 5px/8px 'Montserrat',sans-serif">Neque porro quisquam est, qui dolorem ipsum quia dolor sit amet, consectetur, adipisci</div>
  <div class="abs" style="left:20px;top:405px;width:123px;height:130px;background:#fff"></div>
  <div class="photo" role="img" aria-label="Group celebrating a bachelor party by the pool" style="left:24px;top:407px;width:116px;height:72px;background:linear-gradient(160deg,#8fb8d8,#e8e2d8 55%,#3c3a3e)"></div>
  <div class="abs serif" style="left:24px;top:482px;font-size:7px">Bachelor Parties</div>
  <div class="abs" style="left:24px;top:497px;width:115px;font:400 4px/6px 'Montserrat',sans-serif">Neque porro quisquam est, qui dolorem ipsum quia dolor sit amet, consectetur</div>
  <div class="btn dark" style="left:24px;top:517px;width:44px;height:12px">READ MORE</div>
  <div class="m-arrow" style="left:6px;top:463px">‹</div>
  <div class="m-arrow" style="left:149px;top:463px">›</div>

  <div class="abs" style="left:0;top:565px;width:163px;height:235px;background:linear-gradient(180deg,#2a2a2a,#1f1f1f)"></div>
  <div class="abs center kicker" style="top:578px;color:#fff;font-size:6.5px">We Provide</div>
  <div class="abs center title" style="top:589px;color:#fff;font-size:11px">Custom Packages</div>
  <div class="abs center" style="top:612px;padding:0 10px;color:#ddd;font:400 5px/8px 'Montserrat',sans-serif">Nemo enim ipsam voluptatem quia voluptas sit aspernatur consequuntur</div>
  <div class="photo" role="img" aria-label="Hotel lobby with bright lights" style="left:19px;top:648px;width:125px;height:134px;background:linear-gradient(160deg,#3a4f66,#d8e4ee 50%,#2c2c36)"></div>
  <div class="abs" style="left:36px;top:662px;width:90px;height:114px;background:var(--panel);text-align:center;color:#fff">
    <div class="pkg-icon" style="margin-top:14px;width:24px;height:24px"></div>
    <div style="font:700 6.5px 'Playfair Display',serif;color:var(--gold);margin-top:6px">Lodging</div>
    <div style="font:400 4px/6px 'Montserrat',sans-serif;margin:4px 8px 0;color:#ddd">Sed ut perspiciatis unde omnis natus error sit voluptatem accusantium doloremque</div>
  </div>
  <div class="btn gold" style="left:61px;top:755px;width:40px;height:10px;font-size:4.5px">READ MORE</div>
  <div class="m-arrow w" style="left:6px;top:707px">‹</div>
  <div class="m-arrow w" style="left:149px;top:707px">›</div>

  <div class="abs" style="left:0;top:800px;width:163px;height:155px;background:#fff"></div>
  <div class="abs center title" style="top:810px;font-size:11px">Recent News</div>
  <div class="abs" style="left:0;top:832px;width:163px;height:120px;background:var(--gold)"></div>
  <div class="abs" style="left:0;top:880px;width:163px;height:72px;background:#fff"></div>
  <div class="photo" role="img" aria-label="Evening dinner party with warm lights" style="left:17px;top:846px;width:129px;height:94px;background:linear-gradient(150deg,#2a2218,#6b4a28 50%,#1c1814)"></div>
  <div class="news-item" style="left:30px;top:902px">
    <span class="news-tag">18th Nov</span>
    <span class="news-title" style="font-size:5px;line-height:7px">Nor Again is there anyone who<br>loves or pursues</span>
  </div>
  <div class="m-arrow" style="left:6px;top:884px">‹</div>
  <div class="m-arrow" style="left:149px;top:884px">›</div>

  <div class="abs" style="left:0;top:955px;width:163px;height:407px;background:var(--light)"></div>
  <div class="abs title" style="left:7px;top:965px;font-size:10.5px">Contac Information</div>
  <svg class="abs" style="left:7px;top:996px" width="7" height="9" viewBox="0 0 10 13"><path d="M5 0a5 5 0 0 0-5 5c0 4 5 8 5 8s5-4 5-8a5 5 0 0 0-5-5z" fill="#e0a02e"/><circle cx="5" cy="5" r="2" fill="#fff"/></svg>
  <div class="abs serif" style="left:17px;top:995px;font-size:7px">Address:</div>
  <div class="abs" style="left:7px;top:1014px;font:400 5px/9px 'Montserrat',sans-serif">12 Harbor Lane, Suite 4<br>Port Marlow 40 B11</div>
  <div class="abs" style="left:7px;top:1044px;font:600 5px 'Montserrat',sans-serif">+1 (555) 014 2290</div>
  <div class="abs" style="left:7px;top:1066px;font:600 5px 'Montserrat',sans-serif">info@goldharborconcierge.com</div>
  <div class="abs" style="left:7px;top:1088px;width:148px;height:272px;background:#fff;box-shadow:0 2px 6px rgba(0,0,0,.12)">
    <div class="abs serif" style="left:8px;top:10px;font-size:9px">Reach Us</div>
    <div class="abs" style="left:8px;top:27px;font:400 4.5px 'Montserrat',sans-serif">Nor again is there anyone who pursues</div>
    <div class="m-form-field" style="top:40px">First Name:</div>
    <div class="m-form-field" style="top:66px">Last Name:</div>
    <div class="m-form-field" style="top:92px">Email:</div>
    <div class="m-form-field" style="top:118px">Phone:</div>
    <div class="m-form-field" style="top:144px;height:68px">Comments:</div>
    <div class="submit" style="left:8px;top:222px;width:133px;height:22px">SUBMIT</div>
  </div>

  <div class="abs" style="left:0;top:1362px;width:163px;height:471px;background:linear-gradient(180deg,#262626,#1c1c1c)"></div>
  <div class="abs center brand" style="top:1410px;font-size:11px"><span class="brand-dot"></span>Gold Harbor</div>
  <div class="abs" style="left:7px;top:1458px;color:#fff">
    <div class="serif" style="font-size:9px;margin-bottom:5px">Quick Links</div>
    <div style="font:400 5px/12px 'Montserrat',sans-serif;color:#ddd">Home<br>About Us<br>Services<br>Support<br>News<br>Contact Us</div>
    <div class="serif" style="font-size:9px;margin:12px 0 5px">Services</div>
    <div style="font:400 5px/12px 'Montserrat',sans-serif;color:#ddd">Bachelor Parties<br>Bachelorette Parties<br>Medical Tourism</div>
    <div class="serif" style="font-size:9px;margin:12px 0 5px">Support</div>
    <div style="font:400 5px/12px 'Montserrat',sans-serif;color:#ddd">Airport Transportation<br>Lodging<br>Billingual guides</div>
    <div class="serif" style="font-size:9px;margin:14px 0 7px">Social On</div>
    <div class="social"><span></span><span></span><span></span></div>
  </div>
  <div class="abs center" style="top:1798px;font:400 5px/9px 'Montserrat',sans-serif;color:var(--muted)">Copyright © 2021 <span style="color:#ddd">GOLD HARBOR CONCIERGE</span><br>All rights reserved.</div>
</section>

<!-- ================= DESKTOP ================= -->
<section class="frame desktop" aria-label="Desktop layout">
  <div class="abs hero">
    <div class="photo hero-photo" role="img" aria-label="Friends toasting champagne on a yacht deck at sunset"></div>
    <svg class="abs" style="left:0;top:0" width="584" height="227"><polygon points="345,0 362,0 418,150 410,172" fill="#fff"/><polygon points="500,0 584,0 584,227 398,227 470,60" fill="#fff"/></svg>
    <div class="abs brand" style="left:63px;top:38px;font-size:14px"><span class="brand-dot"></span>Gold Harbor</div>
    <div class="abs hero-kicker">Gold Harbor</div>
    <div class="abs hero-title">Travel Concierge<br>Service</div>
    <div class="abs hero-sub">Sed ut perspiciatis unde omnis iste natus error sit...</div>
    <div class="btn" style="left:63px;top:174px;width:46px;height:13px">READ MORE</div>
    <div class="abs hero-menu"><div class="label">MENU</div>HOME<br>ABOUT US<br>SERVICES<br>SUPPORT<br>NEWS<br>CONTACTS</div>
    <div class="abs hero-contact">+1 (555) 014 2290<br>info@goldharborconcierge.com<div class="addr">12 Harbor Lane, Suite 4<br>Port Marlow 40 B11</div></div>
  </div>

  <div class="abs welcome">
    <div class="photo" role="img" aria-label="Softly lit evening party gathering" style="left:0;top:0;width:584px;height:265px;background:linear-gradient(180deg,rgba(60,60,60,.35),rgba(30,30,30,.2))"></div>
    <div class="abs center kicker" style="top:33px;color:#fff">Welcome To</div>
    <div class="abs center title" style="top:44px;color:#fff">Gold Harbor Concierge</div>
    <div class="abs center para" style="top:75px;padding:0 95px;color:#ddd">Neque porro quisquam est, qui dolorem ipsum quia dolor sit amet, consectetur, adipisci velit, sed quia non numquam eius modi tempora incidunt ut labore et dolore magnam aliquam quaerat voluptatem. Nemo enim ipsam voluptatem quia voluptas sit aspernatur aut odit aut fugit, sed quia consequuntur magni dolores eos qui ratione voluptatem sequi nesciunt exercitationem ullam corporis suscipit laboriosam</div>
    <div class="btn" style="left:266px;top:133px;width:52px;height:14px">READ MORE</div>
  </div>

  <svg class="abs services-bg" width="584" height="380"><polygon points="0,138 584,0 584,380 0,380" fill="#eef2f5"/></svg>
  <div class="abs center kicker" style="top:459px">We Arrange</div>
  <div class="abs center title" style="top:470px">Special Services</div>
  <div class="abs center" style="top:493px;font:400 5px 'Montserrat',sans-serif">Neque porro quisquam est, qui dolorem ipsum quia dolor sit amet, consectetur, adipisci</div>

  <div class="service-card" style="left:65px">
    <div class="photo service-photo" role="img" aria-label="Friends celebrating a bachelor party by the pool" style="background:linear-gradient(160deg,#8fb8d8,#e8e2d8 55%,#3c3a3e)"></div>
    <div class="abs service-name">Bachelor Parties</div>
    <div class="abs service-text">Neque porro quisquam est, qui dolorem ipsum quia dolor sit amet, consectetur</div>
    <div class="btn dark" style="left:3px;top:129px;width:44px;height:13px">READ MORE</div>
  </div>
  <div class="service-card" style="left:228px">
    <div class="photo service-photo" role="img" aria-label="Women at a bachelorette party under pink lights" style="background:linear-gradient(160deg,#c03060,#e0608a 45%,#3a1a3a)"></div>
    <div class="abs service-name">Bachelorette Parties</div>
    <div class="abs service-text">Neque porro quisquam est, qui dolorem ipsum quia dolor sit amet, consectetur</div>
    <div class="btn dark" style="left:3px;top:129px;width:44px;height:13px">READ MORE</div>
  </div>
  <div class="service-card" style="left:387px">
    <div class="photo service-photo" role="img" aria-label="Crowd at a warmly lit evening event" style="background:linear-gradient(160deg,#2a1e18,#8a5a30 50%,#1e1612)"></div>
    <div class="abs service-name">Medical Tourism</div>
    <div class="abs service-text">Neque porro quisquam est, qui dolorem ipsum quia dolor sit amet, consectetur</div>
    <div class="btn dark" style="left:3px;top:129px;width:44px;height:13px">READ MORE</div>
  </div>
  <div class="dots" style="left:93px;top:518px">...</div><div class="dots" style="left:198px;top:678px">...</div>
  <div class="dots" style="left:253px;top:518px">...</div><div class="dots" style="left:357px;top:678px">...</div>
  <div class="dots" style="left:412px;top:518px">...</div><div class="dots" style="left:516px;top:678px">...</div>

  <div class="abs packages">
    <div class="abs center kicker" style="top:32px;color:#fff">We Provide</div>
    <div class="abs center title" style="top:43px;color:#fff">Custom Packages</div>
    <div class="abs center" style="top:68px;font:400 5px 'Montserrat',sans-serif;color:#ddd">Nemo enim ipsam voluptatem quia voluptas sit aspernatur consequuntur</div>

    <div class="pkg" style="left:63px">
      <div class="photo pkg-photo" role="img" aria-label="Airplane taking off at sunset" style="background:linear-gradient(170deg,#9ab0c4,#d8d0c0 60%,#6a6058)"></div>
      <div class="abs pkg-panel"><div class="pkg-icon"></div><div class="pkg-name">Airport Transportation</div><div class="pkg-text">Sed ut perspiciatis unde omnis natus error sit voluptatem accusantium doloremque</div><div class="pkg-plus">+</div></div>
    </div>
    <div class="pkg" style="left:219px">
      <div class="photo pkg-photo" role="img" aria-label="Bright hotel lobby interior" style="background:linear-gradient(160deg,#3a4f66,#d8e4ee 50%,#2c2c36)"></div>
      <div class="abs pkg-panel"><div class="pkg-icon"></div><div class="pkg-name" style="color:var(--gold)">Lodging</div><div class="pkg-text">Sed ut perspiciatis unde omnis natus error sit voluptatem accusantium doloremque</div></div>
      <div class="btn gold" style="left:52px;top:122px;width:42px;height:11px;font-size:4.5px">READ MORE</div>
    </div>
    <div class="pkg" style="left:375px">
      <div class="photo pkg-photo" role="img" aria-label="Guide with travellers in the city" style="background:linear-gradient(160deg,#5a4a3a,#b08a68 55%,#2a2420)"></div>
      <div class="abs pkg-panel"><div class="pkg-icon"></div><div class="pkg-name">Bilingual Guides</div><div class="pkg-text">Sed ut perspiciatis unde omnis natus error sit voluptatem accusantium doloremque</div><div class="pkg-plus">+</div></div>
    </div>
  </div>

  <div class="abs news">
    <div class="abs center title" style="top:28px">Recent News</div>
    <div class="abs" style="left:63px;top:56px;width:229px;height:167px;background:var(--gold)"></div>
    <div class="photo" role="img" aria-label="Banquet hall lit in purple and blue" style="left:92px;top:110px;width:195px;height:150px;background:linear-gradient(160deg,#3a2a8a,#7a5ad0 45%,#1a1450)"></div>
    <div class="news-item" style="left:105px;top:212px">
      <span class="news-tag">18th Nov, 2021</span>
      <span class="news-title">Nor Again is there anyone who<br>loves or pursues</span>
    </div>
    <div class="photo" role="img" aria-label="Guests at an elegant evening dinner" style="left:292px;top:56px;width:229px;height:167px;background:linear-gradient(150deg,#2a2218,#6b4a28 50%,#1c1814)"></div>
    <div class="news-item" style="left:318px;top:158px">
      <span class="news-tag">18th Nov, 2021</span>
      <span class="news-title">Nor Again is there anyone who<br>loves or pursues</span>
    </div>
    <div class="photo" role="img" aria-label="Couple dining by candlelight" style="left:297px;top:228px;width:106px;height:72px;background:linear-gradient(150deg,#3a3028,#7a6048 50%,#201a16)"></div>
    <div class="abs news-title" style="left:297px;top:255px;width:106px;text-align:center">Anyone who loves<br>pursues</div>
    <div class="photo" role="img" aria-label="Friends celebrating at a party" style="left:414px;top:228px;width:107px;height:72px;background:linear-gradient(150deg,#3a2a2a,#8a5a4a 50%,#201818)"></div>
    <div class="abs news-title" style="left:414px;top:255px;width:107px;text-align:center">Nor Again<br>is there anyone</div>
  </div>

  <div class="abs contact">
    <div class="abs title" style="left:63px;top:28px">Contac Information</div>
    <svg class="abs" style="left:63px;top:66px" width="6" height="8" viewBox="0 0 10 13"><path d="M5 0a5 5 0 0 0-5 5c0 4 5 8 5 8s5-4 5-8a5 5 0 0 0-5-5z" fill="#e0a02e"/><circle cx="5" cy="5" r="2" fill="#fff"/></svg>
    <div class="abs serif" style="left:70px;top:65px;font-size:7px">Address:</div>
    <div class="abs" style="left:70px;top:78px;font:400 4.5px/7px 'Montserrat',sans-serif">12 Harbor Lane, Suite 4<br>Port Marlow 40 B11</div>
    <div class="abs" style="left:63px;top:105px;font:600 4.5px/12px 'Montserrat',sans-serif">+1 (555) 014 2290<br>info@goldharborconcierge.com</div>
    <div class="abs form-card">
      <div class="abs serif" style="left:29px;top:27px;font-size:9px">Reach Us</div>
      <div class="abs" style="left:29px;top:43px;font:400 4.5px 'Montserrat',sans-serif">Nor again is there anyone who loves or pursues</div>
      <div class="field" style="left:29px;top:57px;width:120px;height:17px">First Name:</div>
      <div class="field" style="left:29px;top:80px;width:120px;height:17px">Last Name:</div>
      <div class="field" style="left:29px;top:103px;width:120px;height:17px">Email:</div>
      <div class="field" style="left:29px;top:126px;width:120px;height:17px">Phone:</div>
      <div class="field" style="left:154px;top:57px;width:120px;height:63px">Comments:</div>
      <div class="submit" style="left:154px;top:126px;width:120px;height:17px">SUBMIT</div>
    </div>
  </div>

  <div class="abs footer">
    <div class="abs brand" style="left:63px;top:75px;font-size:13px"><span class="brand-dot"></span>Gold Harbor</div>
    <div class="f-col" style="left:192px"><h4>Quick Links</h4><p>Home<br>About Us<br>Services<br>Support<br>News<br>Contact Us</p></div>
    <div class="f-col" style="left:287px"><h4>Services</h4><p>Bachelor Parties<br>Bachelorette Parties<br>Medical Tourism</p></div>
    <div class="f-col" style="left:384px"><h4>Support</h4><p>Airport Transportation<br>Lodging<br>Bilingual guides</p></div>
    <div class="f-col" style="left:472px"><h4>Social On</h4><div class="social"><span></span><span></span><span></span></div></div>
    <div class="abs center" style="top:150px;font:400 4px 'Montserrat',sans-serif;color:var(--muted)">Copyright © 2021 <span style="color:#ddd">GOLD HARBOR CONCIERGE</span>. All rights reserved.</div>
  </div>
</section>

</body>
</html>
```